Korvanta Business Card

Looking for business card ideas. Company name is Korvanta. Have a few basic ideas on attachment. Please submit anything with the logo and general information from attachment.

Industry/Entity Type

Business

```html
<!DOCTYPE html>
<html lang="en">
<head>
<meta charset="utf-8">
<title>Korvanta Business Card</title>
<link rel="stylesheet" href="https://fonts.googleapis.com/css2?family=Open+Sans:wght@400;600&family=Oleo+Script:wght@700&display=swap">
<style>
  :root {
    --page-bg: #2b2b2b;
    --card-white: #ffffff;
    --maroon-deep: #3a0a0a;
    --maroon-mid: #7a1a12;
    --maroon-light: #a8301c;
    --gold: #f2c230;
    --orange: #e8731c;
    --brand-red: #d8241c;
    --ink: #1a1a1a;
    --ink-soft: #333333;
    --grey: #6b6b6b;
    --tagline-band: #3b0d0d;
  }
  * { margin: 0; padding: 0; box-sizing: border-box; }
  html, body {
    width: 1200px; height: 600px; overflow: hidden;
    background: var(--page-bg);
  }
  .canvas {
    position: relative; width: 1200px; height: 600px;
    display: flex; align-items: center; justify-content: center;
  }
  .card {
    position: relative; width: 880px; height: 520px;
    background: var(--card-white);
    font-family: "Open Sans", Arial, sans-serif;
    overflow: hidden;
  }
  .card__header {
    position: absolute; left: 0; top: 0; width: 100%; height: 150px;
    background: linear-gradient(90deg, var(--maroon-deep) 0%, var(--maroon-mid) 40%, var(--maroon-light) 60%, var(--maroon-mid) 80%, var(--maroon-deep) 100%);
  }
  .card__header-line {
    position: absolute; left: 0; top: 142px; width: 100%; height: 8px;
  }
  .brand {
    position: absolute; left: 32px; top: 30px;
    display: flex; align-items: center; gap: 26px;
  }
  .brand__dot {
    width: 100px; height: 100px; border-radius: 50%;
    background: var(--brand-red);
  }
  .brand__name {
    font-weight: 600; font-size: 64px; letter-spacing: 10px;
    color: var(--card-white); line-height: 1;
  }
  .person {
    position: absolute; left: 180px; top: 222px; width: 320px; text-align: center;
  }
  .person__name {
    font-family: "Oleo Script", Georgia, serif; font-weight: 700;
    font-size: 46px; color: var(--ink); line-height: 1.05;
  }
  .person__role {
    font-size: 24px; color: var(--ink-soft); line-height: 1.2;
  }
  .contact {
    position: absolute; left: 574px; top: 205px;
    list-style: none; font-size: 22px; color: var(--ink-soft); line-height: 1.65;
  }
  .tagline {
    position: absolute; left: 0; top: 398px; width: 100%; height: 46px;
    background: var(--tagline-band);
    color: var(--card-white); font-size: 32px; text-align: center; line-height: 46px;
  }
  .address {
    position: absolute; left: 0; top: 450px; width: 100%; text-align: center;
    font-size: 21px; letter-spacing: 6px; color: var(--grey);
  }
  .website {
    position: absolute; left: 0; top: 480px; width: 100%; text-align: center;
    font-size: 21px; letter-spacing: 8px; color: var(--brand-red);
  }
</style>
</head>
<body>
<main class="canvas">
  <article class="card">
    <div class="card__header"></div>
    <svg class="card__header-line" viewBox="0 0 880 8" preserveAspectRatio="none" aria-hidden="true">
      <defs>
        <linearGradient id="accentLine" x1="0" x2="1" y1="0" y2="0">
          <stop offset="0" stop-color="#7a1a12" stop-opacity="0"/>
          <stop offset="0.3" stop-color="#e8731c"/>
          <stop offset="1" stop-color="#f2c230"/>
        </linearGradient>
      </defs>
      <rect x="250" y="0" width="630" height="8" fill="url(#accentLine)"/>
    </svg>

    <div class="brand">
      <span class="brand__dot"></span>
      <span class="brand__name">Korvanta</span>
    </div>

    <div class="person">
      <p class="person__name">Dorian Velasco</p>
      <p class="person__role">Director</p>
    </div>

    <ul class="contact">
      <li>(555) 304-7182 Office</li>
      <li>(555) 418-2690 Cell</li>
      <li>dvelasco@korvanta.org</li>
    </ul>

    <p class="tagline">TAKING THE LOCAL CHURCH TO THE NEXT LEVEL</p>
    <p class="address">2480 N. Halden Ave, Marlow, TX 79540</p>
    <p class="website">www.korvanta.org</p>
  </article>
</main>
</body>
</html>
```